IT’S NOT A CLEANING, IT’S YOUR LIFE! TOP TEN REASONS WHY THIS IS NOT JUST A “CLEANING”

We made a list for our patients to let them know why our hygiene appointments are different than other cleanings. Since this is a lot of information, we would like it easily readable within 4-5 feet but we do not want the post to be HUGE. Please see below:

IT’S NOT A CLEANING, IT’S YOUR LIFE!
TOP TEN REASONS WHY THIS IS NOT JUST A “CLEANING”

10. We make you look better. Healthy teeth and gums are more attractive. Recent studies
show that the smile is the first thing people notice and that people with better looking teeth
are more confident and successful.

9. We can relieve your headaches. During your hygiene visit we evaluate for serious bite
issues, many of which lead to muscle soreness, headaches, and migraines.

8. We check for oral cancer. Oral cancer kills 1 person per hour 24 hours a day. The death rate for oral cancer is higher than cancers we routinely hear about such as cervical, thyroid and skin cancer.

7. We make you smell better. During your hygiene visit we eliminate many of the germs that live under your gum tissue and cause bad breath.

6. We save you money. By utilizing the latest dental technology (digital x-rays, mouth
cameras, and magnification glasses) we can help with early detection of tooth and gum
problems and save you the cost of gum surgery, root canals, and implants.

5. We clean in places you cannot. We clean under the gum line and between teeth where
most of the germs hide and cause dental disease. 40% of the bacteria in your mouth lives in
between your teeth.

4. We prevent pain. We identify tooth decay that can lead to nerve involvement and pain,
root canal, and tooth loss.

3. We save your teeth. Most tooth loss is from periodontal/gum disease. At each visit we
evaluate the health of your gums and bone with our periodontal screening. Periodontal
disease, like high blood pressure, is symptomless until it is in advanced stages.

2. We protect your loved ones. Studies have proven that the bacteria that cause dental
disease can be transmitted from person to person. Think about that the next time you kiss
someone!

1. We prolong life. Researchers have linked the inflammation and infection found in the
mouth to heart attacks, strokes, and Alzheimer’s. By reducing infection in your mouth we can
greatly improve your overall health!

```html
<!DOCTYPE html>
<html lang="en">
<head>
<meta charset="utf-8">
<title>It's Not a Cleaning, It's Your Life!</title>
<link rel="stylesheet" href="https://fonts.googleapis.com/css2?family=Fredoka:wght@600;700&display=swap">
<style>
  :root {
    --sky: #2f97dc;
    --tooth-light: #a9cdef;
    --tooth-mid: #8fbde6;
    --ink: #1f2d3a;
    --white: #ffffff;
  }
  * { box-sizing: border-box; margin: 0; padding: 0; }
  html, body {
    width: 848px;
    height: 1200px;
    overflow: hidden;
    background: var(--sky);
  }
  .poster {
    position: relative;
    width: 848px;
    height: 1200px;
    background: var(--sky);
    overflow: hidden;
    font-family: "Fredoka", "Arial Rounded MT Bold", sans-serif;
    color: var(--white);
    text-transform: uppercase;
  }
  .mascot-art {
    position: absolute;
    left: 62px;
    top: 280px;
    width: 740px;
    height: 960px;
    border-radius: 46% 46% 30% 30% / 30% 30% 14% 14%;
    background: radial-gradient(ellipse at 50% 40%, var(--tooth-light) 0%, var(--tooth-mid) 70%, #7fb2df 100%);
    border: 9px solid var(--ink);
    opacity: 0.95;
  }
  .header {
    position: relative;
    text-align: center;
    padding-top: 10px;
  }
  .headline {
    font-weight: 700;
    font-size: 76px;
    line-height: 74px;
    letter-spacing: 1px;
  }
  .subhead {
    margin-top: 18px;
    font-weight: 700;
    font-size: 26px;
    letter-spacing: 0.3px;
  }
  .reasons {
    position: relative;
    list-style: none;
    padding: 0 28px 0 28px;
    margin-top: 12px;
  }
  .reason {
    font-weight: 600;
    font-size: 17.4px;
    line-height: 26px;
    letter-spacing: -0.1px;
    margin-bottom: 19px;
    text-shadow:
      -1.2px -1.2px 0 var(--ink), 1.2px -1.2px 0 var(--ink),
      -1.2px 1.2px 0 var(--ink), 1.2px 1.2px 0 var(--ink),
      0 1.5px 0 var(--ink), 0 -1.5px 0 var(--ink),
      1.5px 0 0 var(--ink), -1.5px 0 0 var(--ink);
  }
  .reason::after { content: ""; display: block; clear: both; }
  .reason-num {
    float: left;
    font-weight: 700;
    font-size: 60px;
    line-height: 48px;
    margin: 2px 0 0 0;
    letter-spacing: -3px;
  }
</style>
</head>
<body>
<main class="poster">
  <div class="mascot-art" role="img" aria-label="Smiling cartoon tooth mascot illustration behind the list"></div>

  <header class="header">
    <h1 class="headline">It’s not a cleaning<br>It’ s your life!</h1>
    <p class="subhead">Top ten reasons why this is not just a “cleaning”</p>
  </header>

  <ol class="reasons">
    <li class="reason"><span class="reason-num">10</span>. We make you look better. Healthy teeth and gums are more attractive. Recent studies show that the smile is the first thing people notice and that people with better looking teeth are more confident and successful.</li>
    <li class="reason"><span class="reason-num">9</span>. We can relieve your headaches. During your hygiene visit we evaluate for serious bite issues, many of which lead to muscle soreness, headaches, and migraines.</li>
    <li class="reason"><span class="reason-num">8</span>. We check for oral cancer. Oral cancer kills 1 person per hour 24 hours a day. The death rate for oral cancer is higher than cancers we routinely hear about such as cervical, thyroid and skin cancer.</li>
    <li class="reason"><span class="reason-num">7</span>. We make you smell better. During your hygiene visit we eliminate many of the germs that live under your gum tissue and cause bad breath.</li>
    <li class="reason"><span class="reason-num">6</span>. We save you money. By utilizing the latest dental technology (digital x-rays mouth cameras, and magnification glasses) we can help with early detection of tooth and gum problems and save you the cost of gum surgery, root canals, and implants.</li>
    <li class="reason"><span class="reason-num">5</span>. We clean in places you cannot. We clean under the gum line and between teeth where most of the germs hide and cause dental disease. 40% of the bacteria in your mouth lives in between your teeth.</li>
    <li class="reason"><span class="reason-num">4</span>. We prevent pain. We identify tooth decay that can lead to nerve involvement and pain, root canal, and tooth loss.</li>
    <li class="reason"><span class="reason-num">3</span>. We save your teeth. Most tooth loss is from periodontal/gum disease. At each visit we evaluate the health of your gums and bone with our periodontal screening. Periodontal disease, like high blood pressure, is symptomless until it is in advanced stages.</li>
    <li class="reason"><span class="reason-num">2</span>. We protect your loved ones. Studies have proven that the bacteria that cause dental disease can be transmitted from person to person. Think about that the next time you kiss someone!</li>
    <li class="reason"><span class="reason-num">1</span>. We prolong life. Researchers have linked the inflammation and infection found in the mouth to heart attacks, strokes, and Alzheimer’s. By reducing infection in your mouth we can greatly improve your overall health!</li>
  </ol>
</main>
</body>
</html>
```